Single-page, simple & clean, departure board web app

TrellisHop.com provides easy to use train schedule information in Chicago, IL between downtown and Hyde Park. The site has been around for about 3 years and the design has not changed since the weekend hackathon at which it was created. Now, it has a solid user base and is in dire need of a fresh design.
The design should be super-clean and intuitive. It is used by the type of people who love the style and personality of sites like Gravlox. The design should incorporate the maroon color that is used extensively on the existing site. The main features are (1) the train depart times, (2) the fact that different stations can be selected as departure/arrival, (3) the fact that a user can click "earlier trains" or "later trains" to quickly scan the times.
This is a single-page web app that displays static content. The design should reflect that 100% of the users time is spent on the single page. There is no "sign up" process or external aspect. All focus should be used to design the best possible display of train times.
Target Market(s)
24-30 yr old, middle to upper income, opinionated, heavily international
Look and feel
Each slider illustrates characteristics of the customer's brand and the style your logo design should communicate.

```html
<!DOCTYPE html>
<html lang="en">
<head>
<meta charset="utf-8">
<title>TrellisHop – Train Schedule</title>
<link rel="stylesheet" href="https://fonts.googleapis.com/css2?family=Lato:wght@400;700&family=Oswald:wght@400;500&display=swap">
<style>
:root{
  --page:#b4b7bc;
  --card:#e7e8ea;
  --maroon:#96283c;
  --maroon-dark:#741a2b;
  --maroon-light:#a93649;
  --panel:#babcc1;
  --ink:#2b2b2b;
  --muted:#8f9194;
  --rule:#e3e3e3;
  --bar-top:#5b5c5e;
  --bar-bottom:#333436;
  --foot:#6a6c70;
}
*{box-sizing:border-box;margin:0;padding:0}
html,body{width:816px;height:1200px;overflow:hidden;background:var(--page);font-family:"Lato",sans-serif}
.stage{position:absolute;left:0;top:0;width:1000px;height:1470px;transform:scale(.816);transform-origin:0 0}
.app{position:absolute;left:20px;top:30px;width:960px;height:1405px;background:var(--card);border-radius:6px;box-shadow:0 8px 14px rgba(0,0,0,.25)}
.topbar{height:80px;background:linear-gradient(#b13247,#94253a);border-radius:6px 6px 0 0;border-bottom:1px solid #6d1626;position:relative}
.brand{position:absolute;left:30px;top:20px;color:#fff;font-weight:700;font-size:30px;letter-spacing:.2px}
.direction{position:absolute;left:540px;top:21px;width:400px;height:39px;display:flex;border:1px solid #6d1626;border-radius:4px;overflow:hidden}
.direction a{flex:1;display:flex;align-items:center;justify-content:center;color:#fff;font-weight:700;font-size:15px;text-decoration:none;background:linear-gradient(#b23a4e,#a02d41)}
.direction a.active{flex:0 0 180px;background:var(--maroon-dark)}
.board{position:absolute;left:20px;top:100px;width:920px;height:1200px;background:var(--panel);border:1px solid #a9abb0;border-radius:3px}
.stations{height:58px;background:linear-gradient(#a4a6ab,#c6c8cc);display:flex;gap:20px;padding:18px 0 0 19px}
.stations a{width:190px;height:40px;background:linear-gradient(#f4f4f4,#dedfe1);color:#8a8c90;font-weight:700;font-size:15px;display:flex;align-items:center;justify-content:center;text-decoration:none;border-radius:3px 3px 0 0}
.stations a.active{background:#fff;color:#333}
.pager{height:51px;background:#fff;border-bottom:1px solid #cfd0d3;display:flex;justify-content:space-between;align-items:center;padding:0 19px 0 20px}
.pager a{width:140px;height:29px;border:1px solid #b9bbbe;border-radius:3px;background:linear-gradient(#f0f0f0,#dadbdd);color:#999;font-size:14px;display:flex;align-items:center;justify-content:center;text-decoration:none}
.train{position:absolute;left:19px;width:880px;background:#fff;border-radius:4px;overflow:hidden;box-shadow:0 1px 2px rgba(0,0,0,.2)}
.train h2{height:50px;background:linear-gradient(var(--bar-top),var(--bar-bottom));color:#fff;font-size:20px;font-weight:700;padding:13px 0 0 28px}
.stop{display:flex;align-items:center;height:75px;border-bottom:1px solid var(--rule);padding-left:26px}
.stop:last-child{border-bottom:0}
.stop.depart{height:71px;background:var(--maroon);border-bottom:0}
.time{width:206px;font-family:"Oswald",sans-serif;font-size:36px;font-weight:500;color:var(--ink);letter-spacing:-.5px}
.time span{color:var(--muted)}
.depart .time,.depart .time span{color:#fff}
.label{font-size:11px;text-transform:uppercase;color:var(--maroon);letter-spacing:.2px}
.depart .label{color:#fff}
.place{font-size:18px;font-weight:700;color:var(--ink);margin-top:2px}
.depart .place{color:#fff}
.promo{position:absolute;left:109px;top:1095px;width:728px;height:90px;background:linear-gradient(#4a4b4d,#2c2d2f);border:2px solid #1d1d1e;border-radius:2px;overflow:hidden}
.promo .ribbon{position:absolute;left:0;top:0}
.promo .pitch{position:absolute;left:72px;top:20px;width:280px;height:46px;background:linear-gradient(90deg,rgba(255,255,255,.22),rgba(255,255,255,.08));border-radius:3px}
.promo .cta{position:absolute;left:368px;top:22px;width:135px;height:42px;background:linear-gradient(#6cc3ea,#3b9fd0);border:1px solid #2b7fac;border-radius:3px;color:#1e4d66;font-size:13px;font-weight:700;display:flex;align-items:center;justify-content:center}
.promo .sponsor{position:absolute;left:528px;top:20px;color:#fff;font-size:24px;font-weight:700;display:flex;align-items:center;gap:8px}
.promo .sponsor i{width:14px;height:14px;background:#fff;border-radius:50%;display:block}
.promo .tag{position:absolute;left:528px;top:52px;color:#cfd0d2;font-size:13px}
.footer{position:absolute;left:0;top:1335px;width:960px;text-align:center;color:var(--foot);font-size:14px;line-height:17px}
</style>
</head>
<body>
<div class="stage">
  <div class="app">
    <header class="topbar">
      <div class="brand">TrellisHop</div>
      <nav class="direction">
        <a class="active" href="#">To Midway Campus</a>
        <a href="#">To Downtown</a>
      </nav>
    </header>

    <main class="board">
      <nav class="stations">
        <a class="active" href="#">From Millenium</a>
        <a href="#">From Van Buren</a>
        <a href="#">From 11th</a>
      </nav>
      <div class="pager">
        <a href="#">Earlier Trains</a>
        <a href="#">Later Trains</a>
      </div>

      <section class="train" style="top:130px">
        <h2>Train 103</h2>
        <div class="stop depart"><div class="time">05:15 AM</div><div><div class="label">Depart from</div><div class="place">Millenium Station</div></div></div>
        <div class="stop"><div class="time">05:30 <span>AM</span></div><div><div class="label">Arrive at</div><div class="place">51st - 53rd Street</div></div></div>
        <div class="stop"><div class="time">05:31 <span>AM</span></div><div><div class="label">Arrive at</div><div class="place">55th - 56th - 57th Street</div></div></div>
        <div class="stop" style="height:79px"><div class="time">05:33 <span>AM</span></div><div><div class="label">Arrive at</div><div class="place">59th Street</div></div></div>
      </section>

      <section class="train" style="top:500px">
        <h2>Train 305</h2>
        <div class="stop depart"><div class="time">06:28 AM</div><div><div class="label">Depart from</div><div class="place">Millenium Station</div></div></div>
        <div class="stop"><div class="time">06:42 <span>AM</span></div><div><div class="label">Arrive at</div><div class="place">51st - 53rd Street</div></div></div>
        <div class="stop"><div class="time">06:44 <span>AM</span></div><div><div class="label">Arrive at</div><div class="place">55th - 56th - 57th Street</div></div></div>
        <div class="stop" style="height:79px"><div class="time">06:46 <span>AM</span></div><div><div class="label">Arrive at</div><div class="place">59th Street</div></div></div>
      </section>

      <section class="train" style="top:880px">
        <h2>Train 105 EXPRESS</h2>
        <div class="stop depart"><div class="time">06:35 AM</div><div><div class="label">Depart from</div><div class="place">Millenium Station</div></div></div>
        <div class="stop" style="height:79px"><div class="time">06:47 <span>AM</span></div><div><div class="label">Arrive at</div><div class="place">55th - 56th - 57th Street</div></div></div>
      </section>

      <aside class="promo">
        <svg class="ribbon" width="90" height="90" viewBox="0 0 90 90" aria-hidden="true"><polygon points="0,60 60,0 88,0 0,88" fill="#e0448f"/></svg>
        <div class="pitch" role="img" aria-label="Hand-lettered headline asking if you need a web designer"></div>
        <div class="cta">BROWSE NOW</div>
        <div class="sponsor"><i></i>PixelGuild</div>
        <div class="tag">The #1 design marketplace online</div>
      </aside>
    </main>

    <footer class="footer">
      Train Schedule Last Updated: January 15, 2012<br>
      Terms and Conditions of Use | Questions or Comments
    </footer>
  </div>
</div>
</body>
</html>
```